Boutique investment company is looking for money

We, Cardelith, are a very small boutique consulting and investment management firm in SWITZERLAND. Cardelith is trying to raise EUR 5-15 million in areas not easily accessible to private investors.

It will not be possible to raise these funds from traditional institutional investors because:
- Time and budget constraints
- Lack of track record in this particular area
Therefore, the capital has to be raised from in a non-conventional way, guerilla-style, from probably 10-15 private investors providing 1 million each. What can we offer? First, the money will be in Switzerland. Second, it will not be with a large bank – so, discretion is guaranteed. We are no-bullshit but data-driven, out of the box investors. We are different.

The site is only the bait to contact us. Maybe it should look like a presentation, just with additional elements for navigation. Maybe there should be one image or a chart explaining each page.

The site will be small, five pages, in two or three languages each.

Investors in Russia and South America

Boutique

Coded - Design and coding required

4 page

• Read the "Nice to Haves" section

Requirements
Must have
• If you have local insight to Russia and Southern America - use it.
• I am German and I love modern architecture - and I would like to see simple and logical design, including easy navigation.
• I am enclosing some files you may find useful. The graphics need to be consistent and can either be clean like they are now or look improvised and hand-drawn - if you can turn them consistently into that.
• We need a home page that should simply state "Safe, secure, Swiss" and then four pages: About Cardelith, Investment opportunity, Absolute return investing,
• Investment strategy. And the navigation needs to allow to toggle between English, Russian and Spanish.
• Let me help you by providing some examples of the kind of site that I have in mind, crisp, clean, simple (the sites are listed in alphabetical order):
• vemoridge.example
• tulsenfield.example
• quorvanholt.example
• zepharlind.example
• dormivelleco.example
• ketraholm.example
• lurovaspring.example
• pelmorath.example
• wistegrove.example
• fendralwick.example
• orbesquay.example
• jyn-halcrest.example
• Take a look at these and your job will become easier, much easier. They all have the same type of look and feel to them.
• One really cool landing page is here:
• wdlt.example
• Maybe we can do something like on their landing page in our logo with ursae minoris (see pictures)?
• If you use pictures, think Switzerland. Google the following and look at images:
• Matterhorn
• luzern vierwaldstättersee
• mechanical swiss watch
• vault
Nice to have
• Please look at the logo. I like the Sans Serif Fonts, Gill Sans and Helvetica Neue above all. Colors based on the logo are:
• - dark blue R: 0, G: 22, B: 115
• - light blue R: 68, G: 133, B: 212
Should not have
• Unless you feel that the audience loves pompous design, let's keep it straight.

```html
<!DOCTYPE html>
<html lang="en">
<head>
<meta charset="utf-8">
<title>Cardelith – Safe, secure, Swiss</title>
<link href="https://fonts.googleapis.com/css2?family=Open+Sans:wght@400;600;700&display=swap" rel="stylesheet">
<style>
:root{
  --navy:#001673;
  --navy-deep:#0b1a5c;
  --sky:#4485d4;
  --sky-soft:#6a9fe0;
  --ink:#333a48;
  --muted:#6b7280;
  --line:#e3e6ee;
  --paper:#ffffff;
}
*{box-sizing:border-box;margin:0;padding:0}
html,body{width:684px;height:1200px;overflow:hidden}
body{font-family:"Open Sans",Arial,sans-serif;color:var(--ink);background:var(--paper);position:relative}
.site-header{position:absolute;top:0;left:0;width:684px;height:75px;background:var(--paper)}
.brand{position:absolute;left:14px;top:18px;display:flex;align-items:center;gap:7px}
.brand-mark{width:16px;height:16px;background:var(--navy)}
.brand-name{font-size:20px;font-weight:700;color:var(--navy)}
.lang{position:absolute;right:30px;top:4px;font-size:8px;color:var(--navy);display:flex;align-items:center;gap:4px}
.lang-flag{width:14px;height:9px;background:#c8ccd8}
.main-nav{position:absolute;right:14px;top:36px;display:flex;height:34px}
.main-nav a{display:flex;align-items:center;padding:0 11px;font-size:8.5px;color:var(--navy);text-decoration:none}
.main-nav a.active{background:var(--navy);color:#fff}
.hero{position:absolute;top:75px;left:0;width:684px;height:268px;background:linear-gradient(110deg,#7d8694 0%,#b9c1cc 40%,#e2e6ec 70%,#9aa3b2 100%)}
.hero-title{position:absolute;left:62px;top:114px;font-size:37px;font-weight:600;color:#fff;text-shadow:0 1px 4px rgba(0,0,0,.35)}
.hero-arrow{position:absolute;top:124px;width:16px;height:24px;background:var(--sky)}
.hero-arrow.prev{left:0}.hero-arrow.next{right:0}
.welcome{position:absolute;top:360px;left:60px;width:564px;text-align:center}
.welcome h1{font-size:21px;font-weight:600;color:var(--sky)}
.welcome h1 span{color:var(--navy)}
.welcome p{margin-top:14px;font-size:7.5px;line-height:1.55;color:var(--muted)}
.btn{display:inline-block;background:var(--navy);color:#fff;font-size:7px;font-weight:600;padding:7px 11px;text-decoration:none}
.welcome .btn{margin-top:18px}
.services{position:absolute;top:545px;left:0;width:684px;height:255px;background:var(--sky)}
.services h2{text-align:center;margin-top:15px;font-size:20px;font-weight:600;color:#fff}
.service-card{position:absolute;top:56px;width:270px;height:170px;background:var(--navy-deep);display:flex;padding:10px;gap:8px}
.service-card.left{left:60px}.service-card.right{left:352px}
.service-text{width:120px;color:#fff}
.service-text h3{font-size:11px;font-weight:600}
.service-text p{margin-top:8px;font-size:6.5px;line-height:1.5;color:#d7def3}
.service-text .btn{margin-top:10px;background:#fff;color:var(--navy)}
.service-photo{flex:1;background:linear-gradient(160deg,#eef1f5,#b5bfcd)}
.dots{position:absolute;left:0;width:100%;top:236px;display:flex;justify-content:center;gap:5px}
.dots i{width:5px;height:5px;border-radius:50%;background:var(--navy)}
.dots i+i{background:#fff}
.news{position:absolute;top:850px;left:28px;width:628px}
.news h2{font-size:20px;font-weight:600;color:var(--navy)}
.news-grid{margin-top:18px;display:flex;gap:12px}
.news-card{width:148px;border:1px solid var(--line);background:#fff}
.news-photo{height:92px}
.news-card .body{padding:7px 7px 8px}
.news-card h4{font-size:7px;font-weight:700;color:var(--sky)}
.news-card p{margin-top:4px;font-size:6px;line-height:1.5;color:var(--muted)}
.news-meta{margin-top:6px;display:flex;justify-content:space-between;font-size:5.5px;color:var(--muted);border-top:1px solid var(--line);padding-top:4px}
.site-footer{position:absolute;top:1095px;left:0;width:684px;height:78px;background:var(--navy-deep);display:flex;align-items:center;padding:0 30px;gap:16px}
.foot-item{display:flex;align-items:center;gap:8px;color:#c9d3ef;font-size:6.5px;line-height:1.5;flex:1}
.foot-icon{width:28px;height:28px;border-radius:50%;border:1px solid #5d74b8;display:flex;align-items:center;justify-content:center;flex:none}
.bottom-bar{position:absolute;top:1173px;left:0;width:684px;height:27px;display:flex;align-items:center;justify-content:space-between;padding:0 20px;font-size:6px;color:var(--muted)}
.social{display:flex;gap:4px}
.social i{width:11px;height:11px;background:var(--sky)}
</style>
</head>
<body>
<header class="site-header">
  <div class="brand"><span class="brand-mark"></span><span class="brand-name">Cardelith</span></div>
  <div class="lang"><span class="lang-flag"></span>ENGLISH ▾</div>
  <nav class="main-nav">
    <a class="active" href="#">Home</a>
    <a href="#">About Cardelith</a>
    <a href="#">Investment opportunity</a>
    <a href="#">Absolute return investing</a>
    <a href="#">Investment strategy</a>
    <a href="#">Contact Us</a>
  </nav>
</header>

<section class="hero" role="img" aria-label="Photo of business partners in a meeting">
  <div class="hero-title">Safe, secure, Swiss</div>
  <svg class="hero-arrow prev" viewBox="0 0 16 24"><rect width="16" height="24" fill="#4485d4"/><path d="M10 7 5 12l5 5" stroke="#fff" stroke-width="2" fill="none"/></svg>
  <svg class="hero-arrow next" viewBox="0 0 16 24"><rect width="16" height="24" fill="#4485d4"/><path d="M6 7l5 5-5 5" stroke="#fff" stroke-width="2" fill="none"/></svg>
</section>

<section class="welcome">
  <h1>Welcome to <span>Cardelith</span></h1>
  <p>We are a small boutique consulting and investment management firm based in Switzerland. Our work focuses on areas that are not easily accessible to private investors. Capital stays in Switzerland and away from large banks, so discretion is guaranteed. We are data-driven, independent and direct in the way we invest. We keep our investor circle small, we speak openly about risk and return, and we build long relationships based on trust, clear reporting and careful research into every single opportunity we present.</p>
  <a class="btn" href="#">View More About Us</a>
</section>

<section class="services">
  <h2>What We Do</h2>
  <article class="service-card left">
    <div class="service-text">
      <h3>Boutique Consulting</h3>
      <p>Personal advice for private clients who look for clear, independent and discreet guidance on markets that large institutions rarely cover in depth.</p>
      <a class="btn" href="#">READ MORE</a>
    </div>
    <div class="service-photo" role="img" aria-label="Photo of a child climbing stacked books"></div>
  </article>
  <article class="service-card right">
    <div class="service-text">
      <h3>Investment Management</h3>
      <p>Absolute return strategies managed in Switzerland with a small group of private investors, strict risk limits and transparent reporting.</p>
      <a class="btn" href="#">READ MORE</a>
    </div>
    <div class="service-photo" role="img" aria-label="Photo of a team reviewing charts at a desk"></div>
  </article>
  <div class="dots"><i></i><i></i></div>
</section>

<section class="news">
  <h2>LATEST NEWS</h2>
  <div class="news-grid">
    <article class="news-card">
      <div class="news-photo" role="img" aria-label="Photo of a business handshake" style="background:linear-gradient(160deg,#dfe5ee,#8f9bb0)"></div>
      <div class="body"><h4>BOUTIQUE CONSULTING</h4><p>New insight into private markets for our investor circle.</p><div class="news-meta"><span>Admin</span><span>March 10, 2015</span></div></div>
    </article>
    <article class="news-card">
      <div class="news-photo" role="img" aria-label="Photo of business people climbing steps" style="background:linear-gradient(160deg,#eef1f5,#a9b3c2)"></div>
      <div class="body"><h4>BOUTIQUE CONSULTING</h4><p>How absolute return strategies work in volatile years.</p><div class="news-meta"><span>Admin</span><span>March 10, 2015</span></div></div>
    </article>
    <article class="news-card">
      <div class="news-photo" role="img" aria-label="Illustration of green trees growing from hands" style="background:linear-gradient(160deg,#d6e8c8,#6a9a52)"></div>
      <div class="body"><h4>BOUTIQUE CONSULTING</h4><p>Growing capital steadily with a long term approach.</p><div class="news-meta"><span>Admin</span><span>March 10, 2015</span></div></div>
    </article>
    <article class="news-card">
      <div class="news-photo" role="img" aria-label="Photo of a businessman pointing at a screen" style="background:linear-gradient(160deg,#cfd9ea,#5a6e94)"></div>
      <div class="body"><h4>BOUTIQUE CONSULTING</h4><p>Why discretion matters to private investors today.</p><div class="news-meta"><span>Admin</span><span>March 10, 2015</span></div></div>
    </article>
  </div>
</section>

<footer class="site-footer">
  <div class="foot-item"><span class="foot-icon"><svg width="12" height="12" viewBox="0 0 12 12"><path d="M1 6 6 1.5 11 6M2.5 5v5.5h7V5" stroke="#fff" stroke-width="1.2" fill="none"/></svg></span>Private office in Switzerland,<br>visits by appointment only</div>
  <div class="foot-item"><span class="foot-icon"><svg width="12" height="12" viewBox="0 0 12 12"><path d="M3 1.5 5 4 4 5.2c.6 1.3 1.5 2.2 2.8 2.8L8 7l2.5 2-1 1.5C5.5 10.5 1.5 6.5 1.5 2.5z" fill="#fff"/></svg></span>+41 00 000 00 00</div>
  <div class="foot-item"><span class="foot-icon"><svg width="12" height="12" viewBox="0 0 12 12"><rect x="1.5" y="3" width="9" height="6.5" stroke="#fff" fill="none"/><path d="M1.5 3 6 7l4.5-4" stroke="#fff" fill="none"/></svg></span>info@cardelith.example</div>
</footer>

<div class="bottom-bar">
  <span>Copyright © 2015 Cardelith</span>
  <div class="social"><i></i><i></i><i></i><i></i><i></i></div>
</div>
</body>
</html>
```